Quiet Otter non alcohol beer can design

We are after 3 label designs for a new non alcoholic beer company (Quiet Otter). The colours to be used would primarily be a soft pink, blue, and white. Each label would essentially call out one dominant colour and the other two incorporated. Base of the design fun and eye-catching but still a modern clean aesthetic. A guide would be a general tie-dye colour all over the can with bold writing of the style of beer in one of the contrasting colours. Our logo then featuring in one of the secondary colours.
Eg: combined pink, blue and white can with white being dominant pink beer style and blue logo. Colours alternated on other varieties.
The varieties of beer are (HAZY) (RADLER) and (IPA)
Updates
Hi all, thank-you for the many and varied designs. Some have really hit the brief. We will review all tomorrow and get back to you ASAP. Thanks again for the great work and effort.
Target Market(s)
outdoorsy/active/health conscious
Industry/Entity Type
Beverage
Look and feel
Each slider illustrates characteristics of the customer's brand and the style your logo design should communicate.

```html
<!DOCTYPE html>
<html lang="en">
<head>
<meta charset="utf-8">
<title>Quiet Otter – Label Range</title>
<link rel="stylesheet" href="https://fonts.googleapis.com/css2?family=Bebas+Neue&family=Montserrat:wght@400;600&display=swap">
<style>
  :root{
    --blue:#2f5db0;
    --blue-light:#5b86cf;
    --pink:#e4555c;
    --pink-light:#ef8a8e;
    --white:#f3f3f4;
    --ink:#ffffff;
    --page:#ffffff;
  }
  *{box-sizing:border-box;margin:0;padding:0}
  html,body{width:720px;height:1200px;overflow:hidden;background:var(--page)}
  body{
    display:flex;flex-direction:column;justify-content:space-evenly;align-items:center;
    font-family:"Montserrat",sans-serif;
  }
  .label{
    position:relative;width:600px;height:330px;overflow:hidden;
    background:var(--label-bg);color:var(--label-ink);
  }
  .label--hazy{--label-bg:var(--blue);--label-ink:var(--ink);--accent:var(--pink);--accent-ink:#fff;--badge:var(--white)}
  .label--ipa{--label-bg:var(--pink);--label-ink:var(--ink);--accent:var(--blue);--accent-ink:#fff;--badge:var(--white)}
  .label--radler{--label-bg:var(--white);--label-ink:var(--blue);--accent:var(--pink);--accent-ink:#fff;--badge:var(--blue)}

  .brand{
    position:absolute;top:18px;left:190px;width:110px;height:110px;border-radius:50%;
    border:3px solid var(--label-ink);display:flex;align-items:center;justify-content:center;
    text-align:center;font-weight:600;font-size:15px;line-height:1.1;letter-spacing:1px;
    text-transform:uppercase;color:var(--label-ink);
  }
  .label--radler .brand{color:var(--pink);border-color:var(--pink)}
  .blend-badge{
    position:absolute;top:70px;left:34px;width:46px;height:46px;border-radius:50%;
    background:var(--badge);
  }
  .style-name{
    position:absolute;top:118px;left:90px;
    font-family:"Bebas Neue",sans-serif;font-size:104px;line-height:1;letter-spacing:2px;
    color:var(--label-ink);
  }
  .tagline{
    position:absolute;top:222px;left:96px;font-size:10px;letter-spacing:6px;
    text-transform:uppercase;opacity:.55;color:var(--label-ink);
  }
  .mascot{
    position:absolute;top:40px;right:0;width:190px;height:250px;
    background:linear-gradient(160deg,var(--blue-light),var(--pink-light) 55%,var(--blue));
    border-radius:60px 0 0 0;
  }
  .label--hazy .mascot{background:linear-gradient(160deg,var(--pink-light),var(--pink) 50%,#3b4fa0)}
  .stripes{position:absolute;left:0;right:0;bottom:0;height:62px}
  .stripes .rule{position:absolute;left:0;right:0;top:0;height:4px;background:var(--label-ink)}
  .label--radler .stripes .rule{background:var(--blue)}
  .stripes .band{
    position:absolute;left:0;right:0;top:14px;height:32px;background:var(--accent);
    display:flex;align-items:center;padding-left:250px;
    font-size:13px;color:var(--accent-ink);letter-spacing:.5px;
  }
</style>
</head>
<body>

<section class="label label--hazy">
  <div class="brand">Quiet<br>Otter</div>
  <div class="blend-badge" aria-hidden="true"></div>
  <h1 class="style-name">HAZY</h1>
  <p class="tagline">Drink cold</p>
  <div class="mascot" role="img" aria-label="Illustrated mascot animal in pink and blue tones"></div>
  <div class="stripes"><div class="rule"></div><div class="band">50 CL</div></div>
</section>

<section class="label label--ipa">
  <div class="brand">Quiet<br>Otter</div>
  <div class="blend-badge" aria-hidden="true"></div>
  <h1 class="style-name">IPA</h1>
  <p class="tagline">Drink cold</p>
  <div class="mascot" role="img" aria-label="Illustrated mascot animal in pink and blue tones"></div>
  <div class="stripes"><div class="rule"></div><div class="band">50 CL</div></div>
</section>

<section class="label label--radler">
  <div class="brand">Quiet<br>Otter</div>
  <div class="blend-badge" aria-hidden="true"></div>
  <h1 class="style-name">RADLER</h1>
  <div class="mascot" role="img" aria-label="Illustrated mascot animal in pink and blue tones"></div>
  <div class="stripes"><div class="rule"></div><div class="band">50 CL</div></div>
</section>

</body>
</html>
```